Brin-well Tide Port Custom Brokers Limited

Name: Loranda Pascoe
Title: Customs Broker
Address: Shop 9 Fernvale Commercial Complex
227-229 Marrow Lane
Kingston 8
Telephone: (876)
Email: tideportbrin@quillmail.example

```html
<!DOCTYPE html>
<html lang="en">
<head>
<meta charset="utf-8">
<title>Brin-well Tide Port Custom Brokers Limited — Business Card</title>
<link href="https://fonts.googleapis.com/css2?family=Montserrat:wght@400;500;700&family=Roboto:wght@400&display=swap" rel="stylesheet">
<style>
  :root {
    --navy: #0b2b52;
    --gold: #e9a800;
    --silver: #c3c6cc;
    --white: #ffffff;
    --ink: #1b1b1b;
    --backdrop: #1f1d1e;
  }
  html, body {
    margin: 0;
    padding: 0;
    width: 1200px;
    height: 1200px;
    overflow: hidden;
    background: var(--backdrop);
  }
  .canvas {
    position: relative;
    width: 1200px;
    height: 1200px;
  }
  .card {
    position: absolute;
    left: 190px;
    width: 820px;
    height: 469px;
    border-radius: 26px;
    overflow: hidden;
  }
  .card--back {
    top: 90px;
    background: var(--navy);
    display: flex;
    align-items: center;
    justify-content: center;
  }
  .card--front {
    top: 640px;
    background: var(--white);
  }
  .brand {
    display: flex;
    align-items: center;
    gap: 14px;
    font-family: "Montserrat", sans-serif;
    font-weight: 700;
    letter-spacing: 0.5px;
  }
  .brand__dot {
    width: 22px;
    height: 22px;
    border-radius: 50%;
    flex: none;
  }
  .card--back .brand { color: var(--silver); font-size: 34px; }
  .card--back .brand__dot { background: var(--silver); }
  .card--front .brand {
    position: absolute;
    top: 70px;
    right: 60px;
    color: var(--navy);
    font-size: 24px;
  }
  .card--front .brand__dot { background: var(--gold); width: 18px; height: 18px; }
  .person {
    position: absolute;
    left: 60px;
    right: 60px;
    top: 196px;
    font-family: "Montserrat", sans-serif;
  }
  .person__row {
    display: flex;
    align-items: flex-end;
    gap: 16px;
  }
  .person__name {
    margin: 0;
    flex: none;
    color: var(--gold);
    font-weight: 700;
    font-size: 30px;
    line-height: 1.2;
    text-transform: uppercase;
    letter-spacing: 0.5px;
  }
  .rule {
    flex: 1;
    height: 2px;
    margin-bottom: 8px;
    background: var(--gold);
  }
  .person__title {
    margin: 4px 0 0;
    color: var(--navy);
    font-weight: 500;
    font-size: 17px;
    text-transform: uppercase;
    letter-spacing: 0.5px;
  }
  .address {
    position: absolute;
    left: 60px;
    top: 310px;
    display: flex;
    gap: 12px;
    font-family: "Roboto", sans-serif;
    font-size: 16px;
    line-height: 1.45;
    color: var(--ink);
  }
  .contacts {
    position: absolute;
    right: 60px;
    top: 276px;
    font-family: "Roboto", sans-serif;
    font-size: 16px;
    color: var(--ink);
    list-style: none;
    margin: 0;
    padding: 0;
  }
  .contacts li {
    display: flex;
    align-items: center;
    gap: 10px;
    margin-bottom: 8px;
  }
  .icon { width: 16px; height: 16px; flex: none; fill: var(--navy); }
  .band {
    position: absolute;
    left: 0;
    right: 0;
    bottom: 0;
    height: 22px;
    background: var(--gold);
  }
</style>
</head>
<body>
<main class="canvas">
  <section class="card card--back" aria-label="Card back">
    <div class="brand"><span class="brand__dot"></span>Brin-well Tide Port Custom Brokers Ltd.</div>
  </section>

  <section class="card card--front" aria-label="Card front">
    <div class="brand"><span class="brand__dot"></span>Brin-well Tide Port Custom Brokers Ltd.</div>
    <div class="person">
      <div class="person__row">
        <h1 class="person__name">Loranda Pascoe</h1>
        <div class="rule"></div>
      </div>
      <p class="person__title">Customs Broker</p>
    </div>
    <div class="address">
      <svg class="icon" viewBox="0 0 16 16" aria-hidden="true"><path d="M8 1a5 5 0 0 0-5 5c0 3.8 5 9 5 9s5-5.2 5-9a5 5 0 0 0-5-5zm0 7a2 2 0 1 1 0-4 2 2 0 0 1 0 4z"/></svg>
      <div>Shop 9 Fernvale Commercial Complex<br>227-229 Marrow Lane, Kingston 8</div>
    </div>
    <ul class="contacts">
      <li>
        <svg class="icon" viewBox="0 0 16 16" aria-hidden="true"><path d="M3.6 1.5l2.2 2.6-1.3 1.7a9 9 0 0 0 5.7 5.7l1.7-1.3 2.6 2.2-1.4 2.1C7.6 14.4 1.6 8.4 1.5 2.9z"/></svg>
        (876) 000 0000
      </li>
      <li>
        <svg class="icon" viewBox="0 0 16 16" aria-hidden="true"><path d="M1 3h14v10H1zm1.5 1.5L8 9l5.5-4.5v-.3H2.5z"/></svg>
        tideportbrin@quillmail.example
      </li>
    </ul>
    <div class="band"></div>
  </section>
</main>
</body>
</html>
```